Lending Harbor Partners - business cards

we need new business cards for my company.
i've been in business for 25 years.
my wife and I are mortgage brokers.

we just bought the domain for a website with www.bluekeyhomes.example
that could be used in the design also.

On the business card would be
Front card:

Dale Whitcombe
Owner/Loan Officer
Cell: (555) 814-2976
Lending Harbor Partners
4237 Maple Crest Lane
Cedar Glen, CA 90000
Office (555) 430-7152
Fax (555) 430-7159
website www.bluekeyhomes.example

Back of Card:

LHP BRE #0873512 NMLS #528946
Dale Whitcombe BRE # 06739481 NMLS #527314

```html
<!DOCTYPE html>
<html lang="en">
<head>
<meta charset="utf-8">
<title>Lending Harbor Partners – Business Cards</title>
<link rel="stylesheet" href="https://fonts.googleapis.com/css2?family=Tinos:wght@400;700&family=Arimo:wght@400&display=swap">
<style>
  :root {
    --backdrop-top: #7a0f26;
    --backdrop-bottom: #c0163a;
    --navy: #1d2f52;
    --slate-blue: #3f5f8f;
    --link-red: #9b1b2a;
    --sky-light: #d6effa;
    --sky-mid: #7cc3e6;
    --sky-deep: #2f7fb8;
    --band-light: #e6ecef;
    --band-dark: #7f989f;
    --band-shade: #5c7a82;
    --paper: #ffffff;
  }
  * { margin: 0; padding: 0; box-sizing: border-box; }
  html, body { width: 1200px; height: 600px; overflow: hidden; }
  body {
    background: linear-gradient(180deg, var(--backdrop-top), var(--backdrop-bottom));
    position: relative;
  }
  .card {
    position: absolute;
    top: 132px;
    width: 520px;
    height: 336px;
    box-shadow: 0 6px 18px rgba(0,0,0,0.35);
    background: var(--paper);
  }
  .card--front { left: 50px; }
  .card--back { left: 630px; }
  .card svg { display: block; width: 100%; height: 100%; }
  .company-name { font-family: "Tinos", "Times New Roman", serif; font-weight: 700; font-size: 17px; letter-spacing: 0.8px; fill: var(--navy); }
  .mark-name { font-family: "Tinos", "Times New Roman", serif; font-weight: 700; font-size: 11px; letter-spacing: 1px; fill: var(--navy); }
  .person-name { font-family: "Tinos", "Times New Roman", serif; font-size: 16px; letter-spacing: 0.5px; fill: var(--navy); }
  .person-role { font-family: "Arimo", Arial, sans-serif; font-size: 8px; letter-spacing: 0.4px; fill: var(--slate-blue); }
  .contact { font-family: "Tinos", "Times New Roman", serif; font-size: 9.6px; letter-spacing: 0.2px; fill: var(--navy); }
  .contact--web { fill: var(--link-red); }
  .contact--city, .contact--fax { fill: var(--slate-blue); }
  .license { font-family: "Tinos", "Times New Roman", serif; font-size: 12px; letter-spacing: 0.3px; fill: var(--navy); }
  .license--personal { fill: var(--slate-blue); }
</style>
</head>
<body>

<div class="card card--front">
  <svg viewBox="0 0 390 252" xmlns="http://www.w3.org/2000/svg">
    <defs>
      <radialGradient id="globe-front" cx="55%" cy="20%" r="80%">
        <stop offset="0" stop-color="var(--sky-light)"/>
        <stop offset="0.45" stop-color="var(--sky-mid)"/>
        <stop offset="1" stop-color="var(--sky-deep)"/>
      </radialGradient>
      <linearGradient id="band-front" x1="0" y1="0" x2="0" y2="1">
        <stop offset="0" stop-color="var(--band-dark)"/>
        <stop offset="1" stop-color="var(--band-shade)"/>
      </linearGradient>
      <linearGradient id="room-front" x1="0" y1="0" x2="0" y2="1">
        <stop offset="0" stop-color="#f4f7f8"/>
        <stop offset="1" stop-color="var(--paper)"/>
      </linearGradient>
    </defs>
    <rect class="globe-backdrop" width="390" height="252" fill="url(#globe-front)" role="img" aria-label="Soft blue world map backdrop"/>
    <polygon class="house-band house-band--outer" points="0,112 195,42 390,112 390,252 0,252" fill="var(--band-light)"/>
    <polygon class="house-band house-band--inner" points="24,132 195,64 366,132 366,252 24,252" fill="url(#band-front)"/>
    <polygon class="house-interior" points="38,142 195,80 352,142 352,252 38,252" fill="url(#room-front)"/>

    <text class="company-name" x="195" y="36" text-anchor="middle">LENDING HARBOR PARTNERS</text>
    <text class="mark-name" x="195" y="106" text-anchor="middle">LHP</text>

    <text class="person-name" x="195" y="142" text-anchor="middle">DALE WHITCOMBE</text>
    <text class="person-role" x="195" y="155" text-anchor="middle">OWNER / LOAN OFFICER</text>

    <text class="contact contact--web" x="46" y="192">WWW.BLUEKEYHOMES.EXAMPLE</text>
    <text class="contact" x="46" y="206">4237 MAPLE CREST LANE</text>
    <text class="contact contact--city" x="46" y="220">CEDAR GLEN, CA 90000</text>

    <text class="contact" x="344" y="192" text-anchor="end">CELL: (555) 814-2976</text>
    <text class="contact" x="344" y="206" text-anchor="end">OFFICE (555) 430-7152</text>
    <text class="contact contact--fax" x="344" y="220" text-anchor="end">FAX (555) 430-7159</text>
  </svg>
</div>

<div class="card card--back">
  <svg viewBox="0 0 390 252" xmlns="http://www.w3.org/2000/svg">
    <defs>
      <radialGradient id="globe-back" cx="50%" cy="55%" r="75%">
        <stop offset="0" stop-color="var(--sky-light)"/>
        <stop offset="0.5" stop-color="var(--sky-mid)"/>
        <stop offset="1" stop-color="var(--sky-deep)"/>
      </radialGradient>
    </defs>
    <rect class="globe-backdrop" width="390" height="252" fill="url(#globe-back)" role="img" aria-label="Soft blue world map backdrop"/>
    <polyline class="house-band house-band--outer" points="18,252 18,88 195,14 372,88 372,252" fill="none" stroke="var(--band-light)" stroke-width="16"/>
    <polyline class="house-band house-band--inner" points="38,252 38,102 195,36 352,102 352,252" fill="none" stroke="var(--band-dark)" stroke-width="12"/>

    <text class="mark-name" x="195" y="84" text-anchor="middle">LHP</text>
    <text class="license" x="195" y="150" text-anchor="middle">LHP BRE #0873512 NMLS #528946</text>
    <text class="license license--personal" x="195" y="166" text-anchor="middle">DALE WHITCOMBE BRE # 06739481 NMLS #527314</text>
  </svg>
</div>

</body>
</html>
```